Home page concept, possible logo colour change

There is no need to code a home page, we are just looking for concept ideas.
We have had a logo designed for a new company we are starting named Corvenhall Aluminium Windows & Doors. We are manufacturing bullet resistant window frames. We have had logo designed, we like the concept of the design, but the current colours (black and red) may not be the best option, especially when designing the website home page, and how it interacts with the logo colours. I have also attached the first draft of the home page which we are not happy with. The overall design/navigation is good, we have issues with the darkened out primary image and also the amount of red on the page, it just doesn't feel right. As mentioned before we are happy to look at colour changes to the logo.
Number of Pages Required
1 page
Look and feel
Each slider illustrates characteristics of the customer's brand and the style your logo design should communicate.

```html
<!DOCTYPE html>
<html lang="en">
<head>
<meta charset="utf-8">
<title>Corvenhall Aluminium Windows &amp; Doors</title>
<link rel="stylesheet" href="https://fonts.googleapis.com/css2?family=Poppins:wght@300;400;500;600&family=Roboto+Slab:wght@400;500;600;700&display=swap">
<style>
:root{
  --blue:#0066ff;
  --blue-soft:#3f8cff;
  --ink:#1f2a33;
  --text:#333;
  --grey:#7a7a7a;
  --icon:#6b6b6b;
  --tint:#f5f8fd;
  --white:#fff;
  --rule:#cfd4da;
  --badge:#e3e7ec;
}
*{box-sizing:border-box;margin:0;padding:0}
html,body{width:1200px;height:2229px;overflow:hidden;background:var(--white)}
body{position:relative;font-family:"Poppins",sans-serif;color:var(--text)}
.abs{position:absolute}
.slab{font-family:"Roboto Slab",serif}

/* brand */
.brand{display:flex;align-items:center;gap:8px;color:var(--ink);font-weight:600}
.brand-mark{width:14px;height:14px;background:var(--blue);border-radius:50%}
.brand-name{font-size:28px;line-height:1;letter-spacing:-.5px}
.brand-sub{font-size:7.5px;letter-spacing:.4px;text-transform:uppercase;margin-top:3px}

/* header */
.site-header .brand{left:145px;top:30px}
.nav{top:45px;left:540px;font-size:13px;color:#222}
.nav a{color:inherit;text-decoration:none;position:absolute;white-space:nowrap;top:0}
.caret{display:inline-block;border:4px solid transparent;border-top:5px solid #222;border-bottom:0;margin-left:3px;vertical-align:2px}
.btn{background:var(--blue);color:var(--white);display:flex;align-items:center;justify-content:center;text-decoration:none}
.nav-cta{left:925px;top:35px;width:131px;height:39px;font-size:13px;border-radius:3px}

/* hero */
.hero-art{left:0;top:0;width:1200px;height:570px}
.hero-frame{left:119px;top:177px;width:433px;height:292px;border:2px solid var(--white);border-top:none}
.hero-frame::before{content:"";position:absolute;left:33px;top:0;right:-2px;border-top:2px solid var(--white)}
.hero-star{left:103px;top:160px}
.hero-title{left:144px;top:194px;color:var(--white);font-size:36px;font-weight:700;letter-spacing:2px;line-height:42px}
.hero-sub{left:144px;top:289px;color:var(--white);font-size:26px;font-weight:300}
.hero-copy{left:145px;top:327px;width:345px;color:var(--white);font-size:14px;line-height:21px}
.hero-cta{left:144px;top:405px;width:173px;height:39px;font-size:15px;letter-spacing:.3px}

/* features */
.feature{width:220px;text-align:center}
.feature svg{display:block;margin:0 auto}
.feature h3{font-family:"Roboto Slab",serif;font-weight:500;font-size:18px;color:var(--ink);margin-top:18px}
.feature p{font-size:14.5px;color:var(--grey);line-height:21px;margin-top:8px;font-weight:300}

/* range */
.range{left:0;top:865px;width:1200px;height:701px;background:var(--tint);border-top-left-radius:180px}
.range-tag{left:521px;top:906px;width:147px;height:34px;border:2px solid var(--blue);border-top:none;font-size:13px;color:#333;display:flex;align-items:center;justify-content:center}
.range-tag::before{content:"";position:absolute;left:14px;right:-2px;top:0;border-top:2px solid var(--blue)}
.range-star{left:512px;top:897px}
.range-title{left:0;width:1200px;top:958px;text-align:center;font-size:28px;font-weight:600;color:var(--ink)}
.card{top:1034px;width:292px;height:465px;background:var(--white)}
.card-img{position:absolute;left:22px;top:26px;width:248px;height:252px}
.card h3{position:absolute;left:22px;top:302px;font-family:"Roboto Slab",serif;font-size:22px;font-weight:600;color:var(--ink)}
.card p{position:absolute;left:24px;top:340px;width:250px;font-size:13.3px;line-height:21px;color:#444}
.card a{position:absolute;left:22px;top:423px;font-size:15px;font-weight:600;color:var(--blue);text-decoration:none}

/* enquiry */
.enquiry{left:0;top:1566px;width:1200px;height:307px;background:var(--blue);border-bottom-right-radius:220px 200px}
.enquiry h2{position:absolute;left:0;width:1200px;top:60px;text-align:center;color:var(--white);font-family:"Roboto Slab",serif;font-size:28px;font-weight:700}
.enquiry p{position:absolute;left:0;width:1200px;top:105px;text-align:center;color:var(--white);font-size:14.5px;line-height:22px}
.field{position:absolute;top:201px;width:209px;height:38px;background:var(--blue-soft);color:#e6efff;font-size:13px;padding-left:18px;display:flex;align-items:center}
.enquiry-submit{position:absolute;left:859px;top:201px;width:154px;height:38px;background:var(--white);color:#333;font-size:15px;border-radius:3px;display:flex;align-items:center;justify-content:center}

/* footer */
.site-footer .brand{left:145px;top:1993px}
.foot-links{left:429px;top:1978px;font-size:14.5px;color:#444;line-height:31.7px;list-style:none}
.foot-links .current{color:var(--blue);font-weight:600}
.foot-contact{left:639px;top:1978px;font-size:14.5px;color:#444;line-height:26.5px}
.foot-contact strong{font-weight:600;color:#333}
.foot-contact .row{display:flex;align-items:center;gap:6px;margin-left:-12px}
.qa{left:917px;top:1972px;font-size:14.5px;font-weight:600;color:#333}
.badge{left:945px;top:2020px;width:76px;height:68px;background:var(--badge);border-radius:6px}
.foot-rule{left:144px;top:2178px;width:912px;border-top:1px solid var(--rule)}
.copyright{left:145px;top:2194px;font-size:14px;color:#555}
</style>
</head>
<body>

<header class="site-header">
  <div class="abs brand">
    <span class="brand-mark"></span>
    <div><div class="brand-name">Corvenhall</div><div class="brand-sub">Aluminium Windows &amp; Doors</div></div>
  </div>
  <nav class="abs nav">
    <a style="left:0">Home</a>
    <a style="left:67px">Our Products<span class="caret"></span></a>
    <a style="left:183px">Why Corvenhall</a>
    <a style="left:328px">Blog</a>
  </nav>
  <a class="abs btn nav-cta">Make an Enquiry</a>
</header>

<section class="hero">
  <svg class="abs hero-art" viewBox="0 0 1200 570" width="1200" height="570">
    <defs>
      <linearGradient id="heroPhoto" x1="0" y1="0" x2="1" y2="1">
        <stop offset="0" stop-color="#3d6fc4"/>
        <stop offset=".45" stop-color="#7a7f8a"/>
        <stop offset=".75" stop-color="#3a4049"/>
        <stop offset="1" stop-color="#6b4a36"/>
      </linearGradient>
    </defs>
    <polygon role="img" aria-label="Modern house with large dark-framed aluminium windows against blue sky" points="0,108 1200,78 1200,472 178,535 0,547" fill="url(#heroPhoto)"/>
    <polygon points="178,535 1200,472 1200,563" fill="var(--blue)"/>
  </svg>
  <div class="abs hero-frame"></div>
  <svg class="abs hero-star" width="34" height="34" viewBox="0 0 34 34"><path d="M17 0 L19 15 L34 17 L19 19 L17 34 L15 19 L0 17 L15 15 Z" fill="#fff"/></svg>
  <h1 class="abs hero-title slab">BULLET RESISTANT<br>WINDOWS &amp; DOORS</h1>
  <p class="abs hero-sub">Your First Line Of Defense</p>
  <p class="abs hero-copy">Lorem ipsum dolor sit amet, consectetur adipisicing elit, sed do eiusmod tempor incididunt ut labore et dolore magna aliqua.</p>
  <a class="abs btn hero-cta">Make an Enquiry</a>
</section>

<section class="features">
  <div class="abs feature" style="left:260px;top:640px">
    <svg width="44" height="52" viewBox="0 0 44 52"><path d="M22 3 L40 9 V25 C40 37 32 45 22 49 C12 45 4 37 4 25 V9 Z" fill="none" stroke="var(--icon)" stroke-width="4" stroke-linejoin="round"/><path d="M14 26 L20 32 L31 19" fill="none" stroke="var(--icon)" stroke-width="4" stroke-linecap="round" stroke-linejoin="round"/></svg>
    <h3>Premium Protection</h3>
    <p>Lorem ipsum dolor sit<br>amet, consectetur</p>
  </div>
  <div class="abs feature" style="left:505px;top:640px">
    <svg width="50" height="52" viewBox="0 0 50 52"><rect x="3" y="5" width="44" height="44" fill="none" stroke="var(--icon)" stroke-width="4"/><path d="M25 5 V49 M3 27 H47" stroke="var(--icon)" stroke-width="4"/></svg>
    <h3>Aesthetically Designed</h3>
    <p>Lorem ipsum dolor sit<br>amet, consectetur</p>
  </div>
  <div class="abs feature" style="left:757px;top:640px">
    <svg width="94" height="52" viewBox="0 0 94 52"><rect x="28" y="8" width="40" height="28" rx="2" fill="var(--icon)"/><path d="M70 16 H82 L90 26 V36 H70 Z" fill="none" stroke="var(--icon)" stroke-width="3"/><path d="M2 18 H24 M8 25 H24 M2 32 H24" stroke="var(--icon)" stroke-width="3" stroke-linecap="round"/><circle cx="40" cy="40" r="5" fill="#fff" stroke="var(--icon)" stroke-width="3"/><circle cx="80" cy="40" r="5" fill="#fff" stroke="var(--icon)" stroke-width="3"/></svg>
    <h3>Promptly Delviered</h3>
    <p>Lorem ipsum dolor sit<br>amet, consectetur</p>
  </div>
</section>

<section>
  <div class="abs range"></div>
  <div class="abs range-tag">Explore our range</div>
  <svg class="abs range-star" width="20" height="20" viewBox="0 0 34 34"><path d="M17 0 L19 15 L34 17 L19 19 L17 34 L15 19 L0 17 L15 15 Z" fill="var(--blue)"/></svg>
  <h2 class="abs range-title slab">Superior Protection, Sleek Design</h2>

  <article class="abs card" style="left:144px">
    <div class="card-img" role="img" aria-label="Aluminium window frame corner section with glazing" style="background:linear-gradient(160deg,#f4f4f4,#dfe3e3 55%,#b9c3c1)"></div>
    <h3>Product 1</h3>
    <p>Lorem ipsum dolor sit amet, consectetur adipiscing elit, sed do eiusmod tempor incididunt...</p>
    <a>Learn more</a>
  </article>
  <article class="abs card" style="left:454px">
    <div class="card-img" role="img" aria-label="Cutaway of thermally broken aluminium profile" style="background:linear-gradient(160deg,#f2f3f5,#c9ccd2 55%,#5a5f69)"></div>
    <h3>Product 2</h3>
    <p>Lorem ipsum dolor sit amet, consectetur adipiscing elit, sed do eiusmod tempor incididunt...</p>
    <a>Learn more</a>
  </article>
  <article class="abs card" style="left:763px">
    <div class="card-img" role="img" aria-label="Close-up of dark aluminium door hinge and frame" style="background:linear-gradient(150deg,#3b3f44,#7d858d 55%,#b3bcc4)"></div>
    <h3>Product 3</h3>
    <p>Lorem ipsum dolor sit amet, consectetur adipiscing elit, sed do eiusmod tempor incididunt...</p>
    <a>Learn more</a>
  </article>
</section>

<section class="abs enquiry">
  <h2>Receive Customised Quote. Make An Enquiry.</h2>
  <p>Lorem ipsum dolor sit amet, consectetur adipiscing elit, sed do eiusmod<br>tempor incididunt ut labore et dolore magna aliqua.</p>
  <div class="field" style="left:185px">Name</div>
  <div class="field" style="left:410px">Phone / Mobile</div>
  <div class="field" style="left:635px">Email</div>
  <div class="enquiry-submit">Make Enquiry</div>
</section>

<footer class="site-footer">
  <div class="abs brand">
    <span class="brand-mark"></span>
    <div><div class="brand-name">Corvenhall</div><div class="brand-sub">Aluminium Windows &amp; Doors</div></div>
  </div>
  <ul class="abs foot-links">
    <li class="current">Home</li>
    <li>Our Products</li>
    <li>Why Corvenhall</li>
    <li>Blog</li>
    <li>Make an enquiry</li>
  </ul>
  <div class="abs foot-contact">
    <strong>Sydney</strong><br>
    48 Harrow Lane<br>
    Sydney, NSW 2010 AU
    <div style="height:26px"></div>
    <strong style="line-height:20px;display:block">Contact us</strong>
    <div class="row"><svg width="14" height="14" viewBox="0 0 24 24"><path d="M6.6 10.8a15 15 0 0 0 6.6 6.6l2.2-2.2a1 1 0 0 1 1-.25 11.4 11.4 0 0 0 3.6.57 1 1 0 0 1 1 1V20a1 1 0 0 1-1 1A17 17 0 0 1 3 4a1 1 0 0 1 1-1h3.5a1 1 0 0 1 1 1c0 1.25.2 2.45.57 3.6a1 1 0 0 1-.25 1z" fill="var(--blue)"/></svg>: +61 2 5550 1842</div>
    <div class="row"><svg width="14" height="14" viewBox="0 0 24 24"><path d="M2 12 L22 3 L15 22 L11 14 Z" fill="var(--blue)"/></svg>: info@corvenhall.com</div>
  </div>
  <div class="abs qa">Quality Assurance</div>
  <div class="abs badge" role="img" aria-label="Quality certification badge"></div>
  <div class="abs foot-rule"></div>
  <p class="abs copyright">© 2023 - Corvenhall.com - All rights reserved.</p>
</footer>

</body>
</html>
```